MOREVI VEGAN SUSHI

www.morevi-restaurant.de
We are open in 2018 and are an innovative restaurant from Munich. We would like a cool design for our drinks and food menu. It's very simple at the moment. See the File menu. In any case, our logo should appear. On the website we use neutraface as a font. But it's not a must. We are only open in the evening and appeal to a young, upscale audience.

```html
<!DOCTYPE html>
<html lang="de">
<head>
<meta charset="utf-8">
<title>MOREVI Vegan Sushi – Speisekarte</title>
<link rel="stylesheet" href="https://fonts.googleapis.com/css2?family=Nunito+Sans:wght@300;400;600&display=swap">
<style>
  :root {
    --backdrop: #e7e5e1;
    --card: #ffffff;
    --panel: #1f1f1f;
    --pattern: #2c2c2c;
    --text: #e4e4e4;
    --rule: #5c5c5c;
    --brand-red: #e03b23;
    --badge: #fbe2b4;
    --badge-text: #2a2a2a;
  }
  * { box-sizing: border-box; margin: 0; padding: 0; }
  html, body {
    width: 992px; height: 1200px; overflow: hidden;
    background: var(--backdrop);
    font-family: "Nunito Sans", Arial, sans-serif;
  }
  .menu-sheet { position: relative; width: 992px; height: 1200px; }

  .menu-page {
    position: absolute; width: 403px; height: 519px;
    background: var(--card);
    box-shadow: 0 2px 6px rgba(0,0,0,0.18);
  }
  .page-1 { left: 75px;  top: 64px; }
  .page-2 { left: 517px; top: 64px; }
  .page-3 { left: 75px;  top: 623px; }
  .page-4 { left: 517px; top: 621px; }

  .menu-panel {
    position: absolute; left: 22px; top: 23px; width: 358px; height: 472px;
    background: var(--panel);
  }
  .pattern-band {
    position: absolute; left: 0; top: 0; width: 100%; height: 32px;
    background: var(--pattern);
  }
  .brand-tab {
    position: absolute; left: 72px; top: 0; width: 65px; height: 102px;
    background: var(--brand-red);
    display: flex; flex-direction: column; align-items: center; justify-content: center; gap: 8px;
  }
  .brand-mark {
    width: 22px; height: 22px; border-radius: 50%; background: #ffffff;
  }
  .brand-name {
    color: #ffffff; font-size: 8px; font-weight: 400; letter-spacing: 2.5px;
  }

  .menu-content {
    position: absolute; left: 72px; top: 138px; width: 249px;
    color: var(--text);
  }
  .menu-section { margin-bottom: 17px; }
  .section-title {
    display: flex; justify-content: space-between; align-items: baseline;
    font-size: 12px; font-weight: 400; letter-spacing: 0.6px;
    padding-bottom: 4px; border-bottom: 1px solid var(--rule);
    margin-bottom: 6px;
  }
  .section-note { font-size: 7.5px; letter-spacing: 0; }
  .menu-item {
    display: flex; align-items: baseline;
    font-size: 7.6px; font-weight: 300; line-height: 14px;
  }
  .item-name { white-space: nowrap; }
  .item-name.multiline { white-space: normal; line-height: 10.5px; padding: 1.5px 0; }
  .leader {
    flex: 1; margin: 0 2px; border-bottom: 1px dotted #8a8a8a; transform: translateY(-2px);
  }
  .spacer { flex: 1; }
  .price { white-space: nowrap; }

  .allergy-note {
    position: absolute; left: 86px; top: 484px; width: 230px; height: 22px;
    background: var(--badge); color: var(--badge-text);
    display: flex; align-items: center;
  }
  .vegan-label {
    display: flex; align-items: center; gap: 5px;
    font-size: 9px; font-weight: 600; letter-spacing: 0.5px;
    padding: 0 6px 0 12px; border-right: 1px solid #c9b48c; height: 14px;
  }
  .allergy-text { font-size: 4.6px; line-height: 5.6px; padding-left: 5px; }
</style>
</head>
<body>
<main class="menu-sheet">

  <!-- Seite 1: Menüs -->
  <section class="menu-page page-1">
    <div class="menu-panel">
      <div class="pattern-band" role="img" aria-label="Wellenmuster aus Kreisen als oberer Zierstreifen"></div>
      <div class="brand-tab"><span class="brand-mark"></span><span class="brand-name">MOREVI</span></div>
      <div class="menu-content">
        <div class="menu-section">
          <h2 class="section-title">CHEF MENÜ mit Aperitiv <span class="section-note">für 2 Personen</span></h2>
          <p class="menu-item"><span class="item-name">Kleine Portion Ramensuppe Mit Gemüse &amp; Nudeln</span><span class="spacer"></span><span class="price">81,00 €</span></p>
          <p class="menu-item"><span class="item-name">Mini Set</span></p>
          <p class="menu-item"><span class="item-name">Dessert</span></p>
        </div>
        <div class="menu-section">
          <h2 class="section-title">OMAKASE <span class="section-note">für 2 Personen</span></h2>
          <p class="menu-item"><span class="item-name">Edamame</span><span class="spacer"></span><span class="price">68,00 €</span></p>
          <p class="menu-item"><span class="item-name">Omakase Set mit 8 Spezialitäten des Hauses</span></p>
          <p class="menu-item"><span class="item-name">Pana Cotta Mit Beeren</span></p>
        </div>
        <div class="menu-section">
          <h2 class="section-title">SET 1</h2>
          <p class="menu-item"><span class="item-name">Hosomaki</span><span class="spacer"></span><span class="price">33,90 €</span></p>
          <p class="menu-item"><span class="item-name">Futomaki</span></p>
          <p class="menu-item"><span class="item-name">Nigiri</span></p>
          <p class="menu-item"><span class="item-name">Kürbiskroketten</span></p>
          <p class="menu-item"><span class="item-name">Wakame Gurken Salat</span></p>
          <p class="menu-item"><span class="item-name">Pickles</span></p>
          <p class="menu-item"><span class="item-name">Gyoza Teigtaschen</span></p>
          <p class="menu-item"><span class="item-name">Sushi Cake</span></p>
        </div>
      </div>
      <div class="allergy-note">
        <span class="vegan-label">ALL VEGAN</span>
        <span class="allergy-text">Bitte teilen Sie dem Service unbedingt Allergien<br>mit und fragen Sie nach der Allergiker-Menükarte</span>
      </div>
    </div>
  </section>

  <!-- Seite 2: Sets -->
  <section class="menu-page page-2">
    <div class="menu-panel">
      <div class="pattern-band" role="img" aria-label="Wellenmuster aus Kreisen als oberer Zierstreifen"></div>
      <div class="brand-tab"><span class="brand-mark"></span><span class="brand-name">MOREVI</span></div>
      <div class="menu-content">
        <div class="menu-section">
          <h2 class="section-title">SET 2</h2>
          <p class="menu-item"><span class="item-name">Hosomaki</span><span class="spacer"></span><span class="price">31,90 €</span></p>
          <p class="menu-item"><span class="item-name">Futomaki</span></p>
          <p class="menu-item"><span class="item-name">Pickles</span></p>
          <p class="menu-item"><span class="item-name">Sushi “Thuna” Cake</span></p>
          <p class="menu-item"><span class="item-name">Crispy Auberginen mit Mayo</span></p>
          <p class="menu-item"><span class="item-name">Aubergine Dengaku</span></p>
        </div>
        <div class="menu-section">
          <h2 class="section-title">SET 3</h2>
          <p class="menu-item"><span class="item-name">Hosomaki</span><span class="spacer"></span><span class="price">28,90 €</span></p>
          <p class="menu-item"><span class="item-name">Uramaki</span></p>
          <p class="menu-item"><span class="item-name">Nigiri</span></p>
          <p class="menu-item"><span class="item-name">Gemüse Tempura</span></p>
          <p class="menu-item"><span class="item-name">Crispy Tofusticks mit Mayo</span></p>
          <p class="menu-item"><span class="item-name">Wakame Shira Ae</span></p>
        </div>
      </div>
      <div class="allergy-note">
        <span class="vegan-label">ALL VEGAN</span>
        <span class="allergy-text">Bitte teilen Sie dem Service unbedingt Allergien<br>mit und fragen Sie nach der Allergiker-Menükarte</span>
      </div>
    </div>
  </section>

  <!-- Seite 3: Vorspeisen, Sushi, Kleine Gerichte -->
  <section class="menu-page page-3">
    <div class="menu-panel">
      <div class="pattern-band" role="img" aria-label="Wellenmuster aus Kreisen als oberer Zierstreifen"></div>
      <div class="brand-tab"><span class="brand-mark"></span><span class="brand-name">MOREVI</span></div>
      <div class="menu-content">
        <div class="menu-section">
          <h2 class="section-title">VORSPEISEN</h2>
          <p class="menu-item"><span class="item-name">Miso Suppe</span><span class="leader"></span><span class="price">5,50 €</span></p>
          <p class="menu-item"><span class="item-name">Edamame Mit Salz/chili</span><span class="leader"></span><span class="price">4,50 €</span></p>
          <p class="menu-item"><span class="item-name">Seidentofu in hausgemachter Sauce mit Mandeln</span><span class="leader"></span><span class="price">5,50 €</span></p>
        </div>
        <div class="menu-section">
          <h2 class="section-title">SUSHI</h2>
          <p class="menu-item"><span class="item-name">Uramaki mit Tempuragemüse</span><span class="leader"></span><span class="price">8,90 €</span></p>
          <p class="menu-item"><span class="item-name">Futomaki wechselndes Gemüse</span><span class="leader"></span><span class="price">8,00 €</span></p>
          <p class="menu-item"><span class="item-name">Uramaki mit Austernpilze</span><span class="leader"></span><span class="price">7,50 €</span></p>
          <p class="menu-item"><span class="item-name">Hosomaki Gurke Avocado</span><span class="leader"></span><span class="price">5,50 €</span></p>
          <p class="menu-item"><span class="item-name">Hosomaki Gurke Shiitake</span><span class="leader"></span><span class="price">5,50 €</span></p>
          <p class="menu-item"><span class="item-name">Tomaten Nigiri</span><span class="leader"></span><span class="price">4,50 €</span></p>
        </div>
        <div class="menu-section">
          <h2 class="section-title">KLEINE GERICHTE</h2>
          <p class="menu-item"><span class="item-name">Gemüse Tempura</span><span class="leader"></span><span class="price">8,00 €</span></p>
          <p class="menu-item"><span class="item-name">Crispy Tofusticks mit Mayo</span><span class="leader"></span><span class="price">8,00 €</span></p>
          <p class="menu-item"><span class="item-name">Kürbiskroketten mit Tangashu</span><span class="leader"></span><span class="price">7,90 €</span></p>
          <p class="menu-item"><span class="item-name">Sushi “Thuna” Cake</span><span class="leader"></span><span class="price">6,90 €</span></p>
          <p class="menu-item"><span class="item-name">Sushi Cake Classic</span><span class="leader"></span><span class="price">6,00 €</span></p>
          <p class="menu-item"><span class="item-name">Aubergine Dengaku</span><span class="leader"></span><span class="price">5,50 €</span></p>
        </div>
      </div>
      <div class="allergy-note">
        <span class="vegan-label">ALL VEGAN</span>
        <span class="allergy-text">Bitte teilen Sie dem Service unbedingt Allergien<br>mit und fragen Sie nach der Allergiker-Menükarte</span>
      </div>
    </div>
  </section>

  <!-- Seite 4: Hauptspeisen, Dessert -->
  <section class="menu-page page-4">
    <div class="menu-panel">
      <div class="pattern-band" role="img" aria-label="Wellenmuster aus Kreisen als oberer Zierstreifen"></div>
      <div class="brand-tab"><span class="brand-mark"></span><span class="brand-name">MOREVI</span></div>
      <div class="menu-content">
        <div class="menu-section">
          <h2 class="section-title">HAUPTSPEISEN</h2>
          <p class="menu-item"><span class="item-name multiline">Herrlich cremiges Katsu Curry<br>mit knusprigen Auberginensticks, Reis &amp; Pickles</span><span class="leader"></span><span class="price">17,90 €</span></p>
          <p class="menu-item"><span class="item-name">Ramen Suppe mit Nudeln, Gemüse &amp; Tofu</span><span class="leader"></span><span class="price">14,90 €</span></p>
          <p class="menu-item"><span class="item-name">Chirashi Sushi Bowl</span><span class="leader"></span><span class="price">13,90 €</span></p>
          <p class="menu-item"><span class="item-name multiline">Sommersalate mit Sesamdressing &amp;<br>Crispy Tofusticks mit Mayo</span><span class="spacer"></span><span class="price">12,50 €</span></p>
        </div>
        <div class="menu-section">
          <h2 class="section-title">DESSERT</h2>
          <p class="menu-item"><span class="item-name">Cheesecake mit Beeren</span><span class="leader"></span><span class="price">6,50 €</span></p>
          <p class="menu-item"><span class="item-name">Pana Cotta mit Beeren</span><span class="leader"></span><span class="price">5,90 €</span></p>
          <p class="menu-item"><span class="item-name">Sorbet des Tages</span><span class="leader"></span><span class="price">5,50 €</span></p>
          <p class="menu-item"><span class="item-name">Sorbet des Tages mit Schuss</span><span class="leader"></span><span class="price">6,90 €</span></p>
        </div>
      </div>
      <div class="allergy-note">
        <span class="vegan-label">ALL VEGAN</span>
        <span class="allergy-text">Bitte teilen Sie dem Service unbedingt Allergien<br>mit und fragen Sie nach der Allergiker-Menükarte</span>
      </div>
    </div>
  </section>

</main>
</body>
</html>
```